Flyer design

We need a new flyer designed. We are not happy with our current design. We want to keep the pictures and basic info, just new design.

Target Market(s)

primarily multi family and HOA,s

Industry/Entity Type

Construction Company

Requirements
Must have
• Must have photos uploaded and use the text on the previous flyer. (also uploaded)

```html
<!DOCTYPE html>
<html lang="en">
<head>
<meta charset="utf-8">
<title>Corvane Construction Services Flyer</title>
<link rel="stylesheet" href="https://fonts.googleapis.com/css2?family=Lato:wght@400;700;900&family=Questrial&family=Oswald:wght@600&display=swap">
<style>
  :root {
    --blue: #2a93e6;
    --blue-deep: #1858e0;
    --dark: #414141;
    --white: #ffffff;
    --grey-text: #555555;
    --page-bg: #e6e6e6;
  }
  * { margin: 0; padding: 0; box-sizing: border-box; }
  html, body { width: 1200px; height: 1200px; overflow: hidden; background: var(--page-bg); }
  .stage { position: relative; width: 1200px; height: 1200px; }
  .flyer {
    position: absolute; left: 200px; top: 40px;
    width: 924px; height: 1295px;
    transform: scale(0.865); transform-origin: top left;
    background: var(--white);
    font-family: "Lato", sans-serif;
    box-shadow: 0 4px 18px rgba(0,0,0,0.25);
    overflow: hidden;
  }
  .abs { position: absolute; }
  .hero-photo {
    left: 0; top: 0; width: 924px; height: 437px;
    background: linear-gradient(180deg, #ffffff 0%, #f3f7fd 18%, #a9c9f0 34%, #6fa4e6 46%, #55585c 60%, #3b3c3e 80%, #2c2c2d 100%);
  }
  .brand { left: 318px; top: 40px; display: flex; align-items: center; gap: 14px; }
  .brand-mark { width: 60px; height: 60px; background: var(--blue-deep); }
  .brand-name { font-weight: 900; font-size: 56px; color: var(--blue-deep); line-height: 1; }
  .brand-sub { font-family: "Questrial", sans-serif; font-size: 19px; color: var(--grey-text); margin-top: 2px; }
  .blue-band { left: 0; top: 443px; width: 924px; height: 785px; background: var(--blue); }
  .advantage { left: 50px; top: 455px; width: 380px; color: var(--white); }
  .section-title { font-family: "Questrial", sans-serif; font-weight: 700; font-size: 31px; letter-spacing: 0.3px; -webkit-text-stroke: 0.6px currentColor; }
  .rule { height: 3px; background: var(--white); margin-top: 8px; }
  .checklist { list-style: none; }
  .checklist li { position: relative; padding-left: 28px; font-size: 20px; line-height: 26px; }
  .checklist svg { position: absolute; left: 0; top: 6px; width: 20px; height: 18px; }
  .advantage .checklist { margin-top: 14px; }
  .advantage .checklist li { margin-bottom: 14px; }
  .site-photo {
    left: 452px; top: 443px; width: 436px; height: 182px;
    background: linear-gradient(135deg, #c9bdb0 0%, #a89a8c 50%, #6b6f73 100%);
  }
  .interior-photo {
    left: 0; top: 820px; width: 445px; height: 183px;
    background: linear-gradient(90deg, #9a8c7a 0%, #d9cbb4 40%, #c8b79c 70%, #8fa6a8 100%);
  }
  .services { left: 445px; top: 633px; width: 450px; height: 595px; background: var(--dark); color: var(--white); padding: 18px 16px 0 16px; }
  .services .section-title { font-size: 36px; }
  .services .rule { width: 394px; margin-left: 2px; margin-top: 12px; }
  .services .checklist { margin-top: 20px; }
  .services .checklist li { margin-bottom: 10.3px; }
  .call { margin-top: 20px; font-family: "Questrial", sans-serif; font-size: 31px; font-weight: 700; -webkit-text-stroke: 0.6px currentColor; display: flex; align-items: center; gap: 8px; }
  .call svg { width: 32px; height: 32px; }
  .web { font-family: "Questrial", sans-serif; font-size: 27px; margin-top: 4px; }
  .addresses { left: 60px; top: 1030px; color: var(--white); font-size: 20px; line-height: 26px; }
  .addresses h3 { font-size: 18px; font-weight: 700; }
  .addresses p + h3 { margin-top: 6px; }
  .tagline {
    left: 0; top: 1228px; width: 924px; height: 67px;
    display: flex; align-items: center; justify-content: center;
    font-family: "Oswald", sans-serif; font-weight: 600; font-size: 29px;
    color: var(--blue-deep); letter-spacing: -0.3px; white-space: pre;
  }
</style>
</head>
<body>
<svg width="0" height="0" style="position:absolute">
  <defs>
    <symbol id="tick" viewBox="0 0 20 18"><path d="M1 10 L7 16 L19 1 L7 12 Z" fill="currentColor"/></symbol>
  </defs>
</svg>
<div class="stage">
  <div class="flyer">
    <div class="abs hero-photo" role="img" aria-label="Roofers laying new shingles on a large residential roof under a blue sky"></div>
    <div class="abs brand">
      <div class="brand-mark"></div>
      <div>
        <div class="brand-name">Corvane</div>
        <div class="brand-sub">Construction Services Inc.</div>
      </div>
    </div>

    <div class="abs blue-band"></div>

    <section class="abs advantage">
      <h2 class="section-title">The Building Advantage</h2>
      <div class="rule"></div>
      <ul class="checklist">
        <li><svg><use href="#tick"/></svg>Hands on approach</li>
        <li><svg><use href="#tick"/></svg>High level of Communication with Client</li>
        <li><svg><use href="#tick"/></svg>Daily or Weekly Updateson every project</li>
        <li><svg><use href="#tick"/></svg>Competitive Pricing</li>
        <li><svg><use href="#tick"/></svg>Due Diligence</li>
        <li><svg><use href="#tick"/></svg>Single Source for all needs</li>
      </ul>
    </section>

    <div class="abs site-photo" role="img" aria-label="Workers on a lift renovating the facade of a multi-storey building"></div>
    <div class="abs interior-photo" role="img" aria-label="Bright remodeled clubhouse interior with kitchen, lounge seating and lake view"></div>

    <section class="abs services">
      <h2 class="section-title">Services We Provide</h2>
      <div class="rule"></div>
      <ul class="checklist">
        <li><svg><use href="#tick"/></svg>Roof Replacements</li>
        <li><svg><use href="#tick"/></svg>Concrete Repairs</li>
        <li><svg><use href="#tick"/></svg>Consulting Services</li>
        <li><svg><use href="#tick"/></svg>Budget Proposals</li>
        <li><svg><use href="#tick"/></svg>Exterior Siding and Carpentry</li>
        <li><svg><use href="#tick"/></svg>Exterior / Interior Paint</li>
        <li><svg><use href="#tick"/></svg>Office and Clubhouse Remodeling</li>
        <li><svg><use href="#tick"/></svg>Fire and Flood Damage Build Back</li>
        <li><svg><use href="#tick"/></svg>Large Scale Interior Renovations</li>
        <li><svg><use href="#tick"/></svg>Dog Parks</li>
        <li><svg><use href="#tick"/></svg>Asphalt Paving</li>
      </ul>
      <div class="call">Call
        <svg viewBox="0 0 32 32"><circle cx="16" cy="16" r="14" fill="none" stroke="currentColor" stroke-width="2"/><path d="M11 9 l3 0 l1.5 4 l-2 1.5 c1 2.2 2.8 4 5 5 l1.5-2 l4 1.5 l0 3 c-7 1-14-6-13-13z" fill="currentColor"/></svg>
        (555) 210 - 4873</div>
      <div class="web">www.corvaneconstruction.com</div>
    </section>

    <section class="abs addresses">
      <h3>California Address :</h3>
      <p>820 Harbor Ridge Dr. Suite 210<br>Lakeview,CA.90000</p>
      <h3>Texas Address :</h3>
      <p>1450 Cedar Mill Rd.<br>Suite 118-302<br>Oakfield Tx,77000</p>
    </section>

    <div class="abs tagline">GENERAL CONTRACTOR.  MULTIFAMILY. COMMERCIAL. RESIDENTIAL.DUE DILIGENCE</div>
  </div>
</div>
</body>
</html>
```